Lounge Night Poster

We need an attractive poster for our new lounge/night club in San Francisco called Velora Nightclub, promoting our new event, "Coral Night". We will have a live band and Asian singers performing during the night. It is like a lounge where people can chill and have a sip. It will open on July 21.

```html
<!DOCTYPE html>
<html lang="en">
<head>
<meta charset="UTF-8">
<title>Velora Nightclub – Coral Night</title>
<link href="https://fonts.googleapis.com/css2?family=Anton&family=Quicksand:wght@700&family=Neonderthaw&display=swap" rel="stylesheet">
<style>
  :root {
    --bg-deep: #0a0a0a;
    --bg-mid: #1b1b1b;
    --bg-haze: #2b2b2b;
    --bulb-core: #fff4d6;
    --bulb-gold: #f0b860;
    --letter-gold: #a8742f;
    --bulb-glow: rgba(240, 170, 80, .55);
    --rail: #7a3d1c;
    --neon-red: #ff4656;
    --neon-red-glow: #e0102a;
    --neon-yellow: #ffd84a;
    --neon-yellow-glow: #d49a00;
    --date-white: #ffffff;
  }
  * { margin: 0; padding: 0; box-sizing: border-box; }
  html, body {
    width: 900px; height: 1200px; overflow: hidden;
    background: var(--bg-deep);
  }
  .poster {
    position: relative;
    width: 900px; height: 1200px;
    overflow: hidden;
    background: var(--bg-deep);
  }
  .city-bridge-scene {
    position: absolute; inset: 0;
    background:
      radial-gradient(ellipse 60% 25% at 60% 57%, var(--bg-haze) 0%, transparent 70%),
      linear-gradient(180deg, var(--bg-deep) 0%, var(--bg-mid) 48%, var(--bg-deep) 100%);
  }
  .marquee-rails { position: absolute; left: 0; top: 0; }
  .venue-name-block { font-weight: 700; }
  .venue-name {
    position: absolute; left: 0; width: 900px;
    text-align: center;
    font-family: "Quicksand", sans-serif;
    font-weight: 700;
    font-size: 136px;
    line-height: 1;
    letter-spacing: 3px;
    color: transparent;
    background:
      radial-gradient(circle, var(--bulb-core) 0 2.2px, var(--bulb-gold) 3.4px, transparent 4.6px) 0 0 / 13px 13px,
      linear-gradient(180deg, var(--letter-gold), #8a5a22);
    -webkit-background-clip: text;
    background-clip: text;
    filter: drop-shadow(0 0 6px var(--bulb-glow)) drop-shadow(0 0 2px rgba(255,220,150,.5));
  }
  .venue-name.line-one { top: 201px; }
  .venue-name.line-two { top: 382px; }
  .event-title {
    position: absolute; left: 0; width: 900px; top: 500px;
    text-align: center;
    font-family: "Neonderthaw", cursive;
    font-weight: 400;
    font-size: 140px;
    line-height: 1.1;
    padding-left: 30px;
    color: var(--neon-red);
    text-shadow: 0 0 3px #ff8a94, 0 0 10px var(--neon-red-glow), 0 0 24px rgba(224,16,42,.7);
  }
  .guitar-accent {
    position: absolute; left: 240px; top: 646px;
    width: 280px; height: 50px;
    background: radial-gradient(ellipse at center, rgba(255,216,74,.22) 0%, rgba(212,154,0,.08) 55%, transparent 75%);
  }
  .event-tagline {
    position: absolute; left: 278px; top: 672px;
    font-family: "Neonderthaw", cursive;
    font-size: 88px;
    line-height: 1.1;
    color: var(--neon-yellow);
    text-shadow: 0 0 3px #fff0a0, 0 0 10px var(--neon-yellow-glow), 0 0 20px rgba(212,154,0,.6);
  }
  .event-date {
    position: absolute; left: 0; width: 900px; top: 898px;
    text-align: center;
    font-family: "Anton", sans-serif;
    font-size: 106px;
    line-height: 1;
    letter-spacing: 1px;
    color: var(--date-white);
  }
</style>
</head>
<body>
  <main class="poster">
    <div class="city-bridge-scene" role="img" aria-label="Night photograph of a suspension bridge over the bay with city lights in the distance, in dark grey tones"></div>

    <svg class="marquee-rails" width="900" height="1200" viewBox="0 0 900 1200" aria-hidden="true">
      <g stroke="var(--rail)" stroke-width="2" opacity="0.8">
        <line x1="30" y1="229" x2="866" y2="229"/>
        <line x1="30" y1="320" x2="866" y2="320"/>
        <line x1="30" y1="410" x2="866" y2="410"/>
        <line x1="30" y1="501" x2="866" y2="501"/>
      </g>
    </svg>

    <h1 class="venue-name-block">
      <span class="venue-name line-one">VELORA</span>
      <span class="venue-name line-two">NIGHTCLUB</span>
    </h1>

    <h2 class="event-title">Coral Night</h2>

    <div class="guitar-accent" role="img" aria-label="Neon outline of an electric guitar"></div>
    <p class="event-tagline">with live music</p>

    <p class="event-date">JULY 21</p>
  </main>
</body>
</html>
```